Email Signature Design

Please design an email signature, the below is an example of our current design;
___

CARRODY ESTATE HOLDINGS PTY LTD
BENEDICT HARLOWE
Licensed Strata and Community Manager

143 Tallowood Street,
KELDARRA NSW 2093

P: 02.9473.6820 F: 9536.2048
Website: www.carrodyestate.com.au

This e-mail message and accompanying data may contain information that is confidential and private. If you are not the intended recipient, the use, dissemination, distribution or copying of this message or data is prohibited.

If you have received this e-mail in error please notify us immediately and delete all material pertaining to this e-mail. strata@carrodyestate.com.au

___

We would like to incorporate our logo and company colours, you can view the colours and feel of image at www.carrodyestate.com.au

Industry/Entity Type

It Company

Requirements
Must have
• use of logo and company colours (image)

```html
<!DOCTYPE html>
<html lang="en">
<head>
<meta charset="utf-8">
<title>Carrody Estate Holdings – Email Signature</title>
<link rel="stylesheet" href="https://fonts.googleapis.com/css2?family=Open+Sans:wght@300;400;700&family=Arimo:wght@400;700&display=swap">
<style>
  :root {
    --backdrop-light: #ffffff;
    --backdrop-mid: #e4e4e4;
    --backdrop-dark: #8a8a8a;
    --panel-white: #ffffff;
    --panel-grey: #6c6b70;
    --brand-olive: #807c3e;
    --brand-sand: #ddd1a8;
    --text-grey: #6a696e;
    --text-light: #ffffff;
  }
  * { margin: 0; padding: 0; box-sizing: border-box; }
  html, body { width: 1200px; height: 1000px; overflow: hidden; }
  body {
    position: relative;
    font-family: "Open Sans", Arial, sans-serif;
    background:
      radial-gradient(ellipse 900px 700px at 620px 520px, var(--backdrop-light) 35%, rgba(255,255,255,0) 100%),
      linear-gradient(135deg, var(--backdrop-dark) 0%, var(--backdrop-mid) 30%, var(--backdrop-light) 55%, var(--backdrop-mid) 85%, #777 100%);
  }
  .signature-panels { position: absolute; left: 0; top: 0; width: 1200px; height: 1000px; }

  .brand-block { position: absolute; left: 146px; top: 440px; }
  .brand-mark {
    position: absolute; left: 0; top: -96px;
    width: 80px; height: 80px; background: var(--brand-olive);
  }
  .brand-name {
    font-family: "Arimo", Arial, sans-serif;
    font-weight: 700; font-size: 24px; letter-spacing: 0.2px;
    color: var(--text-grey); white-space: nowrap;
    margin-top: 36px;
  }
  .brand-tagline {
    font-family: "Arimo", Arial, sans-serif;
    font-weight: 400; font-size: 19px; letter-spacing: 0.6px;
    color: var(--text-grey); margin-top: 2px; white-space: nowrap;
  }

  .contact-block {
    position: absolute; right: 134px; top: 407px;
    text-align: right; color: var(--text-light);
  }
  .contact-name { font-weight: 700; font-size: 20px; letter-spacing: 0.8px; line-height: 28px; }
  .contact-role { font-weight: 700; font-size: 15.5px; letter-spacing: 0.4px; line-height: 22px; }
  .contact-address { font-weight: 300; font-size: 17px; margin-top: 18px; margin-right: 16px; line-height: 24px; }
  .contact-web { font-weight: 300; font-size: 17px; margin-right: 34px; line-height: 28px; }
</style>
</head>
<body>
  <svg class="signature-panels" viewBox="0 0 1200 1000" aria-hidden="true">
    <defs>
      <filter id="panel-shadow" x="-5%" y="-20%" width="110%" height="140%">
        <feDropShadow dx="2" dy="3" stdDeviation="2.5" flood-color="#000" flood-opacity="0.45"/>
      </filter>
    </defs>
    <polygon points="40,397 572,397 611,545 82,542" fill="var(--panel-white)" filter="url(#panel-shadow)"/>
    <polygon points="578,397 1112,397 1084,545 620,545" fill="var(--panel-grey)" filter="url(#panel-shadow)"/>
  </svg>

  <div class="brand-block">
    <span class="brand-mark"></span>
    <p class="brand-name">CARRODY ESTATE HOLDINGS</p>
    <p class="brand-tagline">STRATA MANAGEMENT SERVICES</p>
  </div>

  <div class="contact-block">
    <p class="contact-name">BENEDICT HARLOWE</p>
    <p class="contact-role">Licensed Strata and Community Manager</p>
    <p class="contact-address">143 Tallowood Street, KELDARRA NSW 2093</p>
    <p class="contact-web">www.carrodyestate.com.au</p>
  </div>
</body>
</html>
```